Ridgeway Patrol Website Design

Hello Designers. I am an agency and am helping a security company get a better look. I have a new logo and a car done up. We are looking for a fresh look using the blue and the gold. Open to a complimentary color.

Here is the old site
https://moravanguard.com/

Here is another design for photos and everything. We weren't sold on it because we wanted to make it simple like the first one.

https://ww2.moravanguard.com/

Attached is also the copy I would like to put on there.

I am looking for tough, competent and simple. Our customers are contruction companies, event planners etc. It has to be clean and easy.

One thing we can't provide yet is photos. We are anticipating photos of our team with arms folded beside the car, close up of the owner with a logo'd shirt on. Pictures of an Ridgeway Patrol job site etc. (which most of the time is construction. They also do Mall security. You can see if you want to use stock photos for now.

I wanted to get the look of the front page done first. Hoping for something really awesome. Have fun.

```html
<!DOCTYPE html>
<html lang="en">
<head>
<meta charset="utf-8">
<title>Ridgeway Patrol — New Brunswick's Security Professionals</title>
<link rel="stylesheet" href="https://fonts.googleapis.com/css2?family=Josefin+Sans:wght@600;700&family=Poppins:wght@400;500;600&display=swap">
<style>
:root{
  --backdrop:#0f2033;
  --navy:#13233a;
  --navy-soft:#1c2f4a;
  --gold:#a07b2b;
  --ink:#1b1b1b;
  --muted:#555;
  --light:#f4f4f4;
  --white:#fff;
}
*{margin:0;padding:0;box-sizing:border-box}
html,body{width:1200px;height:3989px;overflow:hidden;background:var(--backdrop)}
body{position:relative;font-family:"Poppins",sans-serif;color:var(--ink)}
.abs{position:absolute}
.page{position:absolute;left:67px;top:54px;width:1068px;height:3879px;background:var(--white);overflow:hidden}
.page > *{position:absolute}
.h-display{font-family:"Josefin Sans",sans-serif;font-weight:700;line-height:1;white-space:nowrap}
.label{font-family:"Josefin Sans",sans-serif;font-weight:700;color:var(--gold);font-size:12px;line-height:1;white-space:nowrap}
.small{font-size:8px;line-height:1.45;color:var(--muted)}
.btn{background:var(--gold);color:var(--white);font-family:"Josefin Sans",sans-serif;font-weight:700;display:flex;align-items:center;justify-content:center;line-height:1;white-space:nowrap}

.brand{font-family:"Josefin Sans",sans-serif;font-weight:700;color:var(--gold);font-size:12px;white-space:nowrap}
.nav a{position:absolute;font-size:10.5px;color:var(--ink);text-decoration:none;line-height:1;white-space:nowrap}
.nav a.active{color:var(--gold)}

.hero-photo{background:linear-gradient(180deg,#e9eef4 0%,#b9c6d4 25%,#8e9c92 45%,#8d9196 58%,#b9bcc0 78%,#fff 100%)}
.feature .title{font-family:"Josefin Sans",sans-serif;font-weight:700;color:var(--gold);font-size:11.5px;line-height:1;white-space:nowrap}
.feature .small{width:128px;margin-top:4px;color:#333}
.form{background:var(--navy)}
.form .head{background:var(--gold);color:var(--white);font-family:"Josefin Sans",sans-serif;font-weight:700;font-size:20px;display:flex;align-items:center;justify-content:center;height:44px}
.field{position:absolute;left:32px;width:243px;background:var(--navy-soft);color:#dfe4ec;font-size:8px;padding:12px 17px}

.service .ring{position:absolute;width:58px;height:58px;border-radius:50%;border:2px solid var(--gold);background:var(--white);display:flex;align-items:center;justify-content:center}
.service .ring span{width:48px;height:48px;border-radius:50%;background:var(--navy)}
.service .title{position:absolute;font-family:"Josefin Sans",sans-serif;font-weight:700;color:var(--gold);font-size:11.5px;line-height:1;white-space:nowrap}
.service .small{position:absolute;width:128px;color:#333}

.about p{font-size:8px;line-height:1.45;color:#333;margin-bottom:10px}
.success{background:linear-gradient(90deg,#233349 0%,#1a2a40 30%,#13233a 55%,#18283d 100%)}
.stat{position:absolute;width:200px;text-align:center;color:var(--white)}
.stat b{display:block;font-family:"Josefin Sans",sans-serif;font-weight:700;font-size:27px;line-height:1}
.stat span{display:block;font-size:11px;margin-top:5px;color:#d9dee6}
.card{background:var(--white);box-shadow:0 2px 10px rgba(0,0,0,.06)}
.card .photo{position:absolute;left:0;top:0;width:100%}
.card h4{position:absolute;left:25px;font-family:"Josefin Sans",sans-serif;font-weight:700;font-size:13.5px;line-height:1.2;color:var(--ink);white-space:nowrap}
.card .small{position:absolute;left:25px;width:180px}
.social i{position:absolute;width:26px;height:26px;border:1.5px solid var(--white);border-radius:50%}
</style>
</head>
<body>
<div class="page">

  <div class="brand" style="left:176px;top:24px">Ridgeway Patrol</div>
  <nav class="nav" style="left:0;top:0;width:1068px;height:60px">
    <a class="active" style="left:292px;top:26px">Home</a>
    <a style="left:365px;top:26px">Security</a>
    <a style="left:439px;top:26px">Services</a>
    <a style="left:520px;top:26px">Industries</a>
    <a style="left:605px;top:26px">Training</a>
    <a style="left:678px;top:26px">Careers</a>
    <a style="left:743px;top:26px">About</a>
  </nav>
  <div class="btn" style="left:795px;top:17px;width:95px;height:28px;font-size:10.5px;font-weight:600">Contact US</div>

  <div class="hero-photo" role="img" aria-label="City skyline behind a branded patrol car with a security officer in a dark suit" style="left:0;top:185px;width:1068px;height:405px"></div>
  <div class="h-display" style="left:0;top:113px;width:1068px;text-align:center;color:var(--gold);font-size:30px">New Brunswick’s</div>
  <div class="h-display" style="left:0;top:152px;width:1068px;text-align:center;color:var(--navy);font-size:30px">SECURITY PROFESSIONALS</div>

  <div class="label" style="left:0;top:618px;width:1068px;text-align:center;font-size:13px">Why Choose Us</div>
  <div class="h-display" style="left:0;top:654px;width:1068px;text-align:center;color:var(--navy);font-size:20px">WE ARE QUALIFIED &amp; PROFESSIONAL</div>
  <p style="left:267px;top:692px;width:535px;text-align:center;font-size:12px;line-height:1.45;color:#333">We can meet any security need. Ridgeway Patrol is located in Alderbrook, New Brunswick serving all of New Brunswick. We offer complete security services including event security, uniformed security and personal security services.</p>

  <div class="feature" style="left:181px;top:793px">
    <svg class="abs" style="left:0;top:0" width="34" height="38" viewBox="0 0 34 38" fill="none" stroke="#13233a" stroke-width="2"><rect x="3" y="18" width="28" height="16"/><circle cx="17" cy="9" r="6"/><path d="M8 26h18"/></svg>
    <div class="abs" style="left:38px;top:2px;width:140px"><div class="title">Securty Consulting</div><div class="small">Lorem ipsum dolor sit amet, consectetur adipiscing elit</div></div>
  </div>
  <div class="feature" style="left:374px;top:793px">
    <svg class="abs" style="left:0;top:0" width="30" height="38" viewBox="0 0 30 38" fill="none" stroke="#13233a" stroke-width="2"><circle cx="15" cy="10" r="7"/><path d="M3 36c0-9 5-14 12-14s12 5 12 14z"/></svg>
    <div class="abs" style="left:31px;top:2px;width:140px"><div class="title">Private Securty</div><div class="small">Lorem ipsum dolor sit amet, consectetur adipiscing elit</div></div>
  </div>
  <div class="feature" style="left:552px;top:793px">
    <svg class="abs" style="left:0;top:0" width="36" height="36" viewBox="0 0 36 36" fill="none" stroke="#13233a" stroke-width="2"><path d="M18 30 5 17a7 7 0 0 1 13-9 7 7 0 0 1 13 9z"/></svg>
    <div class="abs" style="left:40px;top:2px;width:140px"><div class="title">Always Honest</div><div class="small">Lorem ipsum dolor sit amet, consectetur adipiscing elit</div></div>
  </div>
  <div class="feature" style="left:730px;top:793px">
    <svg class="abs" style="left:0;top:0" width="36" height="36" viewBox="0 0 36 36" fill="none" stroke="#13233a" stroke-width="2.2"><path d="M30 18a12 12 0 1 1-4-9"/><path d="M27 4v6h-6"/><text x="11" y="22" font-size="10" font-family="Poppins,sans-serif" font-weight="600" fill="#13233a" stroke="none">24</text></svg>
    <div class="abs" style="left:41px;top:2px;width:140px"><div class="title">24/7 Support</div><div class="small">Lorem ipsum dolor sit amet, consectetur adipiscing elit</div></div>
  </div>

  <div role="img" aria-label="Security officer in a suit speaking into a radio" style="left:188px;top:916px;width:324px;height:349px;background:linear-gradient(160deg,#13233a 0%,#2b3442 55%,#13233a 100%)"></div>
  <div class="form" style="left:582px;top:916px;width:308px;height:349px">
    <div class="head">Contact For Request</div>
    <div class="field" style="top:70px;height:33px">Name</div>
    <div class="field" style="top:121px;height:31px">Email Id</div>
    <div class="field" style="top:171px;height:90px">How Can Help You?</div>
    <div class="btn" style="position:absolute;left:32px;top:278px;width:243px;height:32px;font-size:16px">Submit</div>
  </div>

  <div role="img" aria-label="Security officer in sunglasses speaking into a radio with a raised hand" style="left:450px;top:1331px;width:618px;height:504px;background:linear-gradient(90deg,#fff 0%,#d8dbe0 22%,#6a6f78 50%,#2f3540 75%,#4b5058 100%)"></div>
  <div class="label" style="left:177px;top:1404px;font-size:11px">Securty Consulting</div>
  <div class="h-display" style="left:174px;top:1437px;color:var(--navy);font-size:20px">SECURTY CONSULTING</div>

  <div class="service" style="left:0;top:0;width:1068px;height:10px">
    <div class="ring" style="left:178px;top:1478px"><span></span></div>
    <div class="title" style="left:247px;top:1485px">Static Security</div>
    <div class="small" style="left:250px;top:1500px">Lorem ipsum dolor sit amet, consectetur adipiscing elit</div>
    <div class="ring" style="left:389px;top:1478px"><span></span></div>
    <div class="title" style="left:459px;top:1485px">Security Patrols</div>
    <div class="small" style="left:462px;top:1500px">Lorem ipsum dolor sit amet, consectetur adipiscing elit</div>

    <div class="ring" style="left:178px;top:1560px"><span></span></div>
    <div class="title" style="left:250px;top:1568px">Investigation</div>
    <div class="small" style="left:250px;top:1583px">Lorem ipsum dolor sit amet, consectetur adipiscing elit</div>
    <div class="ring" style="left:389px;top:1560px"><span></span></div>
    <div class="title" style="left:462px;top:1568px">Retail Security</div>
    <div class="small" style="left:462px;top:1583px">Lorem ipsum dolor sit amet, consectetur adipiscing elit</div>

    <div class="ring" style="left:178px;top:1643px"><span></span></div>
    <div class="title" style="left:248px;top:1650px">Cunsulting</div>
    <div class="small" style="left:250px;top:1665px">Lorem ipsum dolor sit amet, consectetur adipiscing elit</div>
    <div class="ring" style="left:389px;top:1643px"><span></span></div>
    <div class="title" style="left:462px;top:1650px">Crime Scenes</div>
    <div class="small" style="left:462px;top:1665px">Lorem ipsum dolor sit amet, consectetur adipiscing elit</div>
  </div>
  <div class="btn" style="left:178px;top:1728px;width:131px;height:33px;font-size:14px">View More</div>

  <div role="img" aria-label="Security officer in a uniform holding a radio" style="left:181px;top:1870px;width:326px;height:390px;background:linear-gradient(135deg,#2a2f37 0%,#4c525c 60%,#9aa3ad 100%)"></div>
  <div class="label" style="left:627px;top:1901px;font-size:11px">About Us</div>
  <div class="h-display" style="left:627px;top:1930px;color:var(--navy);font-size:21px;line-height:1.2">New Brunswick’s<br>Securty Company</div>
  <div class="about" style="left:627px;top:1998px;width:262px">
    <p>We can meet any security need. Ridgeway Patrol is located in Alderbrook, New Brunswick serving all of New Brunswick. We offer complete security services including event security, uniformed security and personal. security services.</p>
    <p>No detail. will be overlooked. Our employee training – screening process ensures that we have the right peop. professional. employees are given the tools to succeed. · crowd control. to protecting people and property, our team is trained with industry best practices.</p>
    <p>We eliminate the guesswork for you by ensuring that were up-to-date on all the regulations pertaining to public safety compliance.</p>
  </div>
  <div class="btn" style="left:628px;top:2189px;width:132px;height:33px;font-size:14px">Read More</div>

  <div class="success" role="img" aria-label="Dark photo of an officer wearing a security vest, overlaid in navy" style="left:0;top:2293px;width:1068px;height:353px"></div>
  <div class="label" style="left:0;top:2350px;width:1068px;text-align:center;font-size:11px">About Us</div>
  <div class="h-display" style="left:0;top:2382px;width:1068px;text-align:center;color:var(--white);font-size:20px">Our Success</div>
  <p style="left:310px;top:2422px;width:448px;text-align:center;color:#dfe4ec;font-size:12px;line-height:1.4">Sed egestas, ante et vulputate volutpat, eros pede semper est, vitae luctus metus libero eu augue.Morbi purus libero, faucibus adipiscing</p>
  <div class="stat" style="left:119px;top:2515px"><b>69K+</b><span>Total User</span></div>
  <div class="stat" style="left:321px;top:2515px"><b>59K+</b><span>Happy User</span></div>
  <div class="stat" style="left:534px;top:2515px"><b>11+</b><span>Your Exoerience</span></div>
  <div class="stat" style="left:746px;top:2515px"><b>8</b><span>Win Awards</span></div>

  <div style="left:0;top:2646px;width:1068px;height:860px;background:var(--light)"></div>
  <div class="label" style="left:178px;top:2719px;font-size:11px">Project</div>
  <div class="h-display" style="left:178px;top:2752px;color:var(--navy);font-size:21px">Our Project</div>
  <p class="small" style="left:178px;top:2791px;width:265px;color:#444">Sed egestas, ante et vulputate volutpat, eros pede semper est, vitae luctus metus libero eu augue. Morbi purus libero, faucibus adipiscing, commodo quis, gravida id, est. Sed lectus.</p>
  <div class="btn" style="left:179px;top:2850px;width:160px;height:33px;font-size:14px">See All Project</div>

  <div class="card" style="left:555px;top:2722px;width:335px;height:472px">
    <div class="photo" role="img" aria-label="Officer in sunglasses adjusting an earpiece" style="height:363px;background:linear-gradient(135deg,#d7dadd,#8b8f94 45%,#2a2d31)"></div>
    <h4 style="top:382px">Lorem ipsum dolor sit amet,<br>consectetur&nbsp; facilisis.</h4>
    <p class="small" style="top:422px">Sed egestas, ante et vulputate volutpat, eros pede semper est,</p>
  </div>
  <div class="card" style="left:179px;top:2932px;width:336px;height:466px">
    <div class="photo" role="img" aria-label="Close-up of a two-way radio clipped to a belt" style="height:362px;background:linear-gradient(180deg,#eceff2,#c9ccd0 40%,#2a2c30 70%,#3a3d42)"></div>
    <h4 style="top:384px">Lorem ipsum dolor sit amet,<br>consectetur&nbsp; facilisis.</h4>
    <p class="small" style="top:424px">Sed egestas, ante et vulputate volutpat, eros pede semper est,</p>
  </div>

  <div style="left:0;top:3506px;width:1068px;height:373px;background:var(--gold)"></div>
  <div role="img" aria-label="Dark navy panel with a faint officer photo" style="left:178px;top:3460px;width:712px;height:158px;background:linear-gradient(90deg,#13233a,#1d2d44 60%,#13233a)"></div>
  <div class="label" style="left:238px;top:3498px;font-size:10.5px">Need For Some Help ?</div>
  <div class="h-display" style="left:238px;top:3533px;color:var(--white);font-size:19px">Let's Contact Us!</div>
  <div style="left:240px;top:3569px;color:#dfe4ec;font-size:8.5px;white-space:nowrap">Lorem ipsum dolor sit amet, consectetur adipiscing elit utelit.</div>
  <div style="left:546px;top:3523px;width:200px;height:33px;background:var(--white);font-size:8.5px;color:#555;padding:11px 12px">Email Adress</div>
  <div class="btn" style="left:757px;top:3523px;width:94px;height:33px;font-size:11px">Submit Now</div>

  <div class="h-display" style="left:174px;top:3795px;color:var(--white);font-size:23px;line-height:1.05">Ridgeway<br>Patrol</div>
  <div style="left:410px;top:3690px;width:1px;height:150px;background:rgba(255,255,255,.25)"></div>
  <div style="left:674px;top:3690px;width:1px;height:150px;background:rgba(255,255,255,.25)"></div>
  <div class="h-display" style="left:475px;top:3695px;color:var(--white);font-size:12px">Contact Us</div>
  <div style="left:477px;top:3737px;color:var(--white);font-size:8px;line-height:1.35;white-space:nowrap">482 HARBOUR LINE RD.<br>SUITE 7 ALDERBROOK NB E2K 4T6</div>
  <div style="left:477px;top:3769px;color:var(--white);font-size:8px">506.555.0142</div>
  <div style="left:477px;top:3790px;color:var(--white);font-size:8px">team@ridgewaypatrol.example</div>
  <div class="h-display" style="left:739px;top:3694px;color:var(--white);font-size:12px">Follow us Social Media</div>
  <div class="social" style="left:0;top:0;width:1068px;height:10px">
    <i style="left:740px;top:3744px"></i><i style="left:773px;top:3744px"></i><i style="left:807px;top:3744px"></i><i style="left:841px;top:3744px"></i>
  </div>
  <div style="left:741px;top:3797px;color:var(--white);font-size:7.5px;white-space:nowrap">Copyright 2022 - Ridgeway Patrol</div>

</div>
</body>
</html>
```